Business Card Design - Nubrova

Who we are?
Nubrova.com is a new social media platform setup for use by all businesses looking to grow social engagement with their brands, products and services.

What are we after?
We need creative business cards designed which will also feature a new company logo.
After a few attempts to develop business cards internally we felt we didn't achieve the results we were after - see the attached files below.

Our Design Parameters:
Essentially the business card needs to feature a new Nubrova logo.
- The logo needs to have the first letter of Nubrova 'N' within an Tulvo type tile/box.
- The other letters of Nubrova 'ubrova' can be in a specific font that resembles our site look and feel
- We attempted to make the card black and white - see the attached files but other warmer colours may also work - please don't use the wooded background that's featured on the website
- The website is about social integration and sharing of media - it would be great if that could come through in the design of the business cards
- Overall feel - tulvo type look
- Logo must be on one side of the card as per the attached files

- The business card needs to feature our slogal - "Social Media Marketing"
- The business card needs to have credit card dimensions

Refer to www.nubrova-example.com for an overview of the company

Please return the completed business card in PSD format.

Hi All,
Thanks for all the great designs.

I have added additional files with variations of the logos. We prefer for the N to be embossed within a white tile as it appears in the attachments.

Couple of pointers:
As I indicated black/black or black/white front and back would work best for us.

Black front with the logo in white as it appears in the attached files and white back with the logo on one side and contact details etc on the other.
The side with the contact details needs to appear elegant and modern, the logo on the other side can be a bit warmer and playful.

Also what I think would work well on the logo side of the business card is the N blended into the background - almost in the form of a watermark as it appears in the attached file - Logo Sample.pptx (but more subtle).

Pleaes refer to the other files for examples of what we are aiming for.

Thank you all.

Cheers,
Nubrova

• Refer to the attached file for formatting of the business card - logo in full size on one side and Name, title, address, contact details on the other

```html
<!DOCTYPE html>
<html lang="en">
<head>
<meta charset="utf-8">
<title>Nubrova — Business Card Presentation</title>
<link href="https://fonts.googleapis.com/css2?family=Roboto+Condensed:wght@700&family=Roboto:wght@300;400&display=swap" rel="stylesheet">
<style>
  :root {
    --board: #ffffff;
    --band: #231f20;
    --ink: #1a1a1a;
    --muted: #9a9a9a;
    --front-dark: #141213;
    --front-mid: #2a2728;
    --white: #ffffff;
    --watermark: rgba(255, 255, 255, 0.06);
    --shadow: rgba(0, 0, 0, 0.28);
    --card-edge: #d8d8d8;
  }
  * { margin: 0; padding: 0; box-sizing: border-box; }
  html, body {
    width: 1200px;
    height: 928px;
    overflow: hidden;
    background: var(--board);
  }
  .board {
    position: relative;
    width: 1200px;
    height: 928px;
    background: var(--board);
  }

  .card {
    position: absolute;
    width: 492px;
    height: 278px;
    box-shadow: 6px 10px 16px var(--shadow);
    overflow: hidden;
  }

  /* Front card */
  .card--front {
    left: 155px;
    top: 110px;
    background: radial-gradient(ellipse at 50% 45%, var(--front-mid) 0%, var(--front-dark) 75%);
  }
  .watermark-tile {
    position: absolute;
    left: 176px;
    top: 49px;
    width: 140px;
    height: 140px;
    border-radius: 14px;
    background: var(--watermark);
  }
  .slogan {
    position: absolute;
    left: 0;
    right: 0;
    top: 113px;
    text-align: center;
    font-family: "Roboto Condensed", sans-serif;
    font-weight: 700;
    font-size: 32px;
    letter-spacing: 1.5px;
    color: var(--white);
  }
  .web {
    position: absolute;
    left: 0;
    right: 0;
    top: 231px;
    text-align: center;
    font-family: "Roboto", sans-serif;
    font-weight: 400;
    font-size: 17px;
    color: var(--white);
  }

  /* Back card */
  .card--back {
    left: 584px;
    top: 361px;
    background: var(--white);
    border: 1px solid var(--card-edge);
  }
  .wordmark {
    position: absolute;
    display: flex;
    align-items: center;
    font-family: "Roboto Condensed", sans-serif;
    font-weight: 700;
    line-height: 1;
  }
  .wordmark .tile { display: block; }
  .card--back .wordmark {
    left: 31px;
    top: 115px;
    gap: 5px;
    font-size: 38px;
    color: var(--ink);
  }
  .card--back .wordmark .tile {
    width: 40px;
    height: 40px;
    background: var(--ink);
  }
  .contact {
    position: absolute;
    left: 272px;
    top: 63px;
    font-family: "Roboto", sans-serif;
    font-weight: 300;
    font-size: 13.5px;
    line-height: 17px;
    color: var(--ink);
  }
  .contact .name { font-weight: 400; font-size: 14px; }
  .contact .role { color: var(--muted); }
  .contact .group { margin-top: 10px; }
  .contact .email { color: var(--muted); }

  /* Bottom band */
  .band {
    position: absolute;
    left: 0;
    top: 723px;
    width: 1200px;
    height: 205px;
    background: var(--band);
  }
  .band .wordmark {
    right: 86px;
    top: 57px;
    gap: 10px;
    font-size: 96px;
    color: var(--white);
  }
  .band .wordmark .tile {
    width: 88px;
    height: 88px;
    background: var(--white);
  }
</style>
</head>
<body>
  <main class="board">
    <section class="card card--front" aria-label="Card front">
      <span class="watermark-tile" aria-hidden="true"></span>
      <p class="slogan">SOCIAL MEDIA MARKETING</p>
      <p class="web">nubrova.com</p>
    </section>

    <section class="card card--back" aria-label="Card back">
      <div class="wordmark"><span class="tile"></span><span>NUBROVA</span></div>
      <div class="contact">
        <p class="name">Marcus Delwyn</p>
        <p class="role">Business Development Manager</p>
        <div class="group">
          <p>0400 555 318</p>
          <p>1300 555 046</p>
        </div>
        <div class="group">
          <p>41-43 Harlow Street</p>
          <p>Eastbrook 3099</p>
        </div>
        <div class="group">
          <p class="email">marcus@nubrova.com</p>
        </div>
      </div>
    </section>

    <footer class="band">
      <div class="wordmark"><span class="tile"></span><span>NUBROVA</span></div>
    </footer>
  </main>
</body>
</html>
```